Yummy Website Re-Design

We have a good website but no VERY GOOD :)

We would like improve the user experience, in shopping page particularly.

Target Market(s)

people 25-40 70% of girl (actually)

Industry/Entity Type

Shopping

Requirements
Must have
• Redesign of www.brunorla.ch
Same colors
Same logotype

1) Homepage
- With highlight product / offer (large display!)
- Space to explain the concept
- Delicious button call-to-action for order a breakfast

2) THE CONCEPT
- Page for explain the concept and team pictures (3persons)

3) COMPOSE !
- Shopping page with, on the top, the X package we offer (business pack, st valentine, christmas, family, etc.) (slider?)

- Then, the products (grid?) classified into categories, we would'like to display one photo / item, the name, the weight and the price.

If you want to add the product, you must choose the number of elements and add to cart

Please, suscribe and test the order process to view all step

4) DELIVERY ZONES
- Page with map of different delivery rate and possibility

5) FAQ

X) Footer with the same information what www.brunorla.ch

Yummy, delicious design (we delivery very delicious breakfast @home).

LET'S EXPLODE YOUR CREATIVITY WITH THIS WORDS : YUMMY, DELICIOUS, SWEET.

```html
<!DOCTYPE html>
<html lang="en">
<head>
<meta charset="utf-8">
<title>Brunorla – Breakfast Delivered</title>
<link rel="stylesheet" href="https://fonts.googleapis.com/css2?family=Cinzel:wght@400;700&family=Crimson+Text:ital,wght@0,400;1,400&display=swap">
<style>
  :root {
    --bar-dark: #1c1a18;
    --logo-dark: #141312;
    --tan: #b08a62;
    --nav-tan: #c9a06c;
    --gold: #d99a2b;
    --gold-light: #f0b63c;
    --gold-line: #a77a3c;
    --brown-panel: rgba(92, 64, 38, 0.84);
    --brown-deep: #3a2a1c;
    --footer-top: #151311;
    --footer-bottom: #4a3422;
    --input-brown: #6b4a2e;
    --copper: #c8894a;
    --white: #ffffff;
  }
  * { box-sizing: border-box; margin: 0; padding: 0; }
  html, body { width: 1200px; height: 749px; overflow: hidden; background: var(--bar-dark); }
  .page { position: relative; width: 1200px; height: 749px; overflow: hidden; font-family: 'Crimson Text', Georgia, serif; }

  .hero-photo {
    position: absolute; left: 0; top: 51px; width: 1200px; height: 587px;
    background: linear-gradient(160deg, #b07a4e 0%, #c89a72 40%, #e2cfb6 75%, #eee6da 100%);
  }

  .topbar { position: absolute; left: 0; top: 0; width: 1200px; height: 51px; background: var(--bar-dark); border-bottom: 1px solid #2a2522; }

  .logo-box {
    position: absolute; left: 144px; top: 0; width: 262px; height: 130px;
    background: linear-gradient(180deg, #1d1b19 0%, var(--logo-dark) 100%);
    border-bottom: 3px solid var(--gold-line);
    box-shadow: 0 6px 14px rgba(0,0,0,0.55);
    display: flex; align-items: center; justify-content: center; gap: 10px;
  }
  .brand-name { font-family: 'Cinzel', Georgia, serif; font-weight: 700; color: var(--tan); font-size: 38px; letter-spacing: 0.5px; }
  .brand-dot { width: 12px; height: 12px; border-radius: 50%; background: var(--tan); }

  .main-nav { position: absolute; left: 434px; top: 6px; height: 42px; display: flex; border-bottom: 1px solid var(--gold-line); }
  .main-nav a {
    font-family: 'Cinzel', Georgia, serif; font-size: 17px; color: var(--nav-tan); text-decoration: none;
    padding: 8px 12px 0 12px; border-left: 1px solid #3a332d; line-height: 1.2; white-space: nowrap;
  }
  .main-nav a.home { padding-left: 22px; padding-right: 20px; }

  .search {
    position: absolute; left: 828px; top: 57px; width: 180px; height: 24px;
    background: rgba(30,27,24,0.88); display: flex; align-items: center; justify-content: space-between; padding: 0 8px;
  }
  .search span { font-family: 'Crimson Text', Georgia, serif; font-style: italic; font-size: 11px; color: var(--nav-tan); }

  .hero-panel {
    position: absolute; left: 135px; top: 288px; width: 551px; height: 259px;
    background: var(--brown-panel); box-shadow: 0 0 18px rgba(0,0,0,0.35);
  }
  .hero-panel::before, .hero-panel::after { content: ""; position: absolute; left: 0; right: 0; height: 1px; background: var(--gold-line); }
  .hero-panel::before { top: 12px; }
  .hero-panel::after { bottom: 30px; }
  .hero-title {
    position: absolute; left: 0; width: 540px; top: 30px; text-align: center;
    font-family: 'Cinzel', Georgia, serif; color: var(--white); font-size: 49px; line-height: 54px; font-weight: 700;
    text-shadow: 2px 3px 3px rgba(0,0,0,0.85);
  }
  .hero-sub {
    position: absolute; left: 0; width: 540px; top: 152px; text-align: center;
    font-family: 'Cinzel', Georgia, serif; color: var(--white); font-size: 21px; line-height: 26px;
    text-shadow: 1px 2px 2px rgba(0,0,0,0.7);
  }
  .hero-sub strong { font-size: 25px; font-weight: 700; }
  .hero-base { position: absolute; left: 8px; right: 0; bottom: 0; height: 10px; background: #2c2622; }

  .order-btn {
    position: absolute; left: 291px; top: 513px; width: 247px; height: 57px;
    background: linear-gradient(180deg, var(--gold-light) 0%, var(--gold) 100%);
    border: 3px solid #7b4f14; border-radius: 6px;
    box-shadow: inset 0 0 0 2px #f7cf72, 0 4px 8px rgba(0,0,0,0.5);
    display: flex; align-items: center; justify-content: center;
    font-family: 'Cinzel', Georgia, serif; font-weight: 700; font-size: 19px; color: var(--brown-deep); text-decoration: none;
  }

  .connect {
    position: absolute; left: 873px; top: 608px; width: 158px; height: 30px; background: var(--white);
    display: flex; align-items: center; gap: 4px; padding: 0 5px;
  }
  .connect em { font-family: 'Crimson Text', Georgia, serif; font-size: 11px; color: #9c7a55; margin-right: 8px; }
  .connect .social { width: 22px; height: 20px; background: #a8966f; border-radius: 2px; }

  .site-footer {
    position: absolute; left: 0; top: 638px; width: 1200px; height: 111px;
    background: linear-gradient(180deg, var(--footer-top) 0%, var(--footer-bottom) 100%);
    border-top: 2px solid var(--gold-line);
  }
  .footer-links { position: absolute; left: 147px; top: 35px; font-size: 15px; color: var(--white); word-spacing: 2px; }
  .copyright { position: absolute; left: 147px; top: 61px; font-family: Arial, Helvetica, sans-serif; font-size: 11px; color: var(--copper); }
  .newsletter-title { position: absolute; left: 487px; top: 20px; font-size: 17px; color: var(--white); }
  .newsletter-field {
    position: absolute; left: 484px; top: 44px; width: 321px; height: 29px; background: var(--input-brown);
    font-size: 15px; color: #f1e6d8; padding: 3px 8px;
  }
  .newsletter-go { position: absolute; left: 801px; top: 41px; width: 35px; height: 35px; }
  .footer-brand { position: absolute; left: 883px; top: 26px; display: flex; align-items: center; gap: 8px; }
  .footer-brand .brand-name { font-size: 30px; color: #8e6e4e; }
  .footer-brand .brand-dot { background: #8e6e4e; width: 10px; height: 10px; }
</style>
</head>
<body>
<div class="page">
  <div class="hero-photo" role="img" aria-label="Large photo of a hearty breakfast plate"></div>

  <header class="topbar">
    <nav class="main-nav">
      <a class="home" href="#">Home</a>
      <a href="#">The Concept</a>
      <a href="#">Compose!</a>
      <a href="#">Delivery Zones</a>
      <a href="#">FAQ</a>
    </nav>
  </header>

  <div class="logo-box">
    <span class="brand-name">Brunorla</span>
    <span class="brand-dot"></span>
  </div>

  <div class="search">
    <span>Search Products &amp; Recipes</span>
    <svg width="11" height="11" viewBox="0 0 11 11" aria-hidden="true">
      <circle cx="6.5" cy="4.5" r="3.3" fill="none" stroke="#c9a06c" stroke-width="1.4"/>
      <line x1="4.2" y1="6.8" x2="1" y2="10" stroke="#c9a06c" stroke-width="1.6"/>
    </svg>
  </div>

  <section class="hero-panel">
    <h1 class="hero-title">YUMMY<br>DELICIOUS, SWEET</h1>
    <p class="hero-sub">We deliver very delicious breakfast<br>@ <strong>HOME</strong></p>
    <div class="hero-base"></div>
  </section>
  <a class="order-btn" href="#">Order A Breakfast</a>

  <div class="connect">
    <em>Connect</em>
    <span class="social"></span><span class="social"></span><span class="social"></span><span class="social"></span>
  </div>

  <footer class="site-footer">
    <div class="footer-links">Welcome &nbsp;-&nbsp; Prepare Your Lil BF &nbsp;-&nbsp; Delivery Area</div>
    <div class="copyright">Copyright © 2012 Brunorla.  All rights reserved.</div>
    <div class="newsletter-title">Subscribe To Our Newsletter</div>
    <div class="newsletter-field">Enter Your Email Address</div>
    <svg class="newsletter-go" viewBox="0 0 35 35" aria-hidden="true">
      <circle cx="17.5" cy="17.5" r="16" fill="#0e0d0c" stroke="#6b4a2e" stroke-width="2"/>
      <polyline points="15,11 21,17.5 15,24" fill="none" stroke="#ffffff" stroke-width="2"/>
    </svg>
    <div class="footer-brand">
      <span class="brand-name">Brunorla</span>
      <span class="brand-dot"></span>
    </div>
  </footer>
</div>
</body>
</html>
```